Book cover for modern/pop-culture-oriented poetry collection

We need a simple, streamlined book-cover design (that'll ultimately be 1600 x 2500 pixels; 300 dpi) for a book of poems. We would like to see three elements on the cover: (1) the title in all caps (GLASSHOURS); (2) the author name in all caps (MIRA VENTO); (3) the main image (attached, slugged "glasshours image"). Image and text should be centered on the cover.

Target Market(s)

Readers of contemporary poetry

Font styles to use
Sans Serif

Requirements
Must have
• Book title, author name, attached photo
Nice to have
• Also attached is the cover of a book (HARBOUR) that is in the style/spirit of what we're looking for.

```html
<!DOCTYPE html>
<html lang="en">
<head>
<meta charset="utf-8">
<title>Glasshours — Mira Vento</title>
<link rel="stylesheet" href="https://fonts.googleapis.com/css2?family=Bebas+Neue&family=Oswald:wght@200&display=swap">
<style>
  :root {
    --page-bg: #ffffff;
    --cover-bg: #ecebe9;
    --cover-edge: #dcdad7;
    --title-ink: #0d0d0d;
    --author-ink: #9a9a9a;
    --image-wood: #6b4a2f;
    --image-glass: #b9bcb3;
  }
  * { margin: 0; padding: 0; box-sizing: border-box; }
  html, body {
    width: 1188px;
    height: 1200px;
    overflow: hidden;
    background: var(--page-bg);
  }
  .stage {
    position: relative;
    width: 1188px;
    height: 1200px;
    display: flex;
    align-items: center;
    justify-content: center;
  }
  .book-cover {
    position: relative;
    width: 720px;
    height: 1125px;
    background: var(--cover-bg);
    border: 1px solid var(--cover-edge);
    display: flex;
    flex-direction: column;
    align-items: center;
  }
  .cover-image {
    margin-top: 150px;
    width: 330px;
    height: 430px;
    border-radius: 4px;
    background: radial-gradient(ellipse at 50% 42%, var(--image-glass) 0%, #9c9686 32%, var(--image-wood) 62%, rgba(107,74,47,0.35) 100%);
  }
  .book-title {
    margin-top: 118px;
    font-family: "Bebas Neue", "Oswald", sans-serif;
    font-size: 128px;
    line-height: 1;
    letter-spacing: 1px;
    color: var(--title-ink);
  }
  .book-author {
    margin-top: 150px;
    font-family: "Oswald", sans-serif;
    font-weight: 200;
    font-size: 62px;
    line-height: 1;
    letter-spacing: 2px;
    color: var(--author-ink);
  }
</style>
</head>
<body>
  <main class="stage">
    <section class="book-cover">
      <div class="cover-image" role="img" aria-label="glasshours image: a vintage wood-cabinet television set on tapered legs with a pale grey screen"></div>
      <h1 class="book-title">GLASSHOURS</h1>
      <p class="book-author">MIRA VENTO</p>
    </section>
  </main>
</body>
</html>
```